Camp Thornbury Retreat Brochure

We are looking for someone to design a brochure/flyer that we can use to promote renting our camp facility. We don't have a specific size in mind, we are open to different options.

The link below has pictures that can be used (don't expect you to use all of them). It also has a PDF of the information that will need to be included in the brochure.

https://files.quillbox.example/folders/7KpR2-TmXa9LwQzB4nYcHd8-vUe3Fs6?usp=sharing

We are a Christian camp and retreat facility. You might want to check out our website to get a feel for what we do.

This brochure will be used to help us increase our rental business. Usually given to an organizational leader who is planning a retreat.

Target Market(s)

Church groups, community groups

Industry/Entity Type

Rental

Requirements
Must have
• Pictures
Information that was included
Website
Contact Information
Nice to have
• Logo
Should not have
• Cross
Clip art

```html
<!DOCTYPE html>
<html lang="en">
<head>
<meta charset="utf-8">
<title>Camp Thornbury Retreat Brochure</title>
<link href="https://fonts.googleapis.com/css2?family=Oswald:wght@500;600&family=Mulish:wght@300;400&display=swap" rel="stylesheet">
<style>
  :root {
    --backdrop: #e6e8e8;
    --forest-dark: #0e1d14;
    --forest-mid: #2f4a3b;
    --pine: #1d5a26;
    --mint: #8fd0a8;
    --mint-deep: #5fae82;
    --mint-pale: #d9f0e2;
    --paper: #ffffff;
    --ink: #1c1c1c;
    --wood: #b07a45;
    --sunset: #e9b98a;
  }
  * { box-sizing: border-box; margin: 0; padding: 0; }
  html, body { width: 1200px; height: 900px; overflow: hidden; background: var(--backdrop); }
  .brochure {
    position: absolute; left: 105px; top: 60px;
    width: 990px; height: 780px;
    display: flex; box-shadow: 0 10px 30px rgba(0,0,0,.18);
  }
  .panel { position: relative; width: 330px; height: 100%; overflow: hidden; background: var(--paper); }

  /* Events panel */
  .interior-photo {
    position: absolute; inset: 0 0 auto 0; height: 520px;
    background:
      linear-gradient(90deg, rgba(255,255,255,.85) 0%, rgba(255,255,255,.2) 55%, rgba(255,255,255,0) 100%),
      linear-gradient(180deg, #9c6a3a 0%, #c89a68 22%, #e3c9a8 45%, rgba(255,255,255,0) 95%),
      linear-gradient(90deg, #f2ebe2 0%, #caa07a 70%, #a9774b 100%);
  }
  .events { position: absolute; left: 40px; top: 235px; }
  .events__title { font: 600 26px/1 "Oswald", sans-serif; color: var(--pine); letter-spacing: .5px; }
  .events__list { list-style: none; margin: 12px 0 0 30px; font: 400 17px/1.3 "Mulish", sans-serif; color: var(--ink); }

  .ground {
    position: absolute; left: 0; right: 0; bottom: 0; height: 180px;
    background: linear-gradient(180deg, rgba(143,208,168,0) 0%, #5f9a7a 28%, var(--forest-dark) 62%);
  }
  .hex { position: absolute; }
  .hex--cabins { left: 140px; bottom: 28px; }
  .hex--pavilion { left: 55px; top: 30px; }

  /* Contact panel */
  .book {
    position: absolute; left: 105px; top: 250px; width: 125px; height: 180px;
    background: var(--mint); text-align: center; padding-top: 20px;
  }
  .book__title { font: 600 46px/1 "Oswald", sans-serif; color: var(--pine); }
  .book__sub { font: 500 16px/1.1 "Oswald", sans-serif; color: var(--pine); }
  .book__call { font: 500 17px/1 "Oswald", sans-serif; color: var(--paper); margin-top: 52px; }
  .contact { position: absolute; left: 0; right: 0; top: 442px; text-align: center; }
  .contact__phone { font: 300 44px/1 "Mulish", sans-serif; color: var(--mint); }
  .contact__or {
    display: inline-block; margin-top: 10px; width: 120px;
    background: var(--mint-pale); font: 300 30px/1.15 "Mulish", sans-serif; color: var(--paper);
  }
  .contact__label { font: 500 16px/1 "Oswald", sans-serif; color: var(--mint-deep); margin-top: 8px; }
  .contact__email { font: 400 15px/1.3 "Mulish", sans-serif; color: var(--mint-deep); margin-top: 2px; }
  .location {
    position: absolute; left: 0; right: 0; bottom: 0; height: 150px;
    background: linear-gradient(180deg, rgba(143,208,168,0) 0%, rgba(143,208,168,.7) 15%, var(--forest-mid) 42%);
    text-align: center; color: var(--mint-pale); padding-top: 58px;
  }
  .location__title { font: 500 18px/1 "Oswald", sans-serif; color: var(--mint); }
  .location__address { font: 300 13px/1.5 "Mulish", sans-serif; margin-top: 6px; }
  .location__web { font: 300 15px/1 "Mulish", sans-serif; margin-top: 14px; }

  /* Cover panel */
  .panel--cover { background: var(--forest-dark); }
  .cover-photo {
    position: absolute; inset: 0 0 150px 0;
    background:
      radial-gradient(ellipse 60% 40% at 70% 30%, rgba(255,214,160,.7) 0%, rgba(255,214,160,0) 70%),
      linear-gradient(180deg, #efd9bd 0%, var(--sunset) 28%, #8a8a5e 55%, #3f5a3a 78%, var(--forest-dark) 100%);
  }
  .brand {
    position: absolute; top: 90px; left: 0; right: 0; text-align: center;
    font: 600 28px/1 "Oswald", sans-serif; color: var(--forest-dark); letter-spacing: 1px;
  }
  .social { position: absolute; right: 70px; bottom: 70px; display: flex; gap: 14px; }
  .social span { width: 28px; height: 28px; border-radius: 50%; background: var(--paper); }
</style>
</head>
<body>
<main class="brochure">

  <section class="panel panel--events">
    <div class="interior-photo" role="img" aria-label="Photo of a wooden cabin interior with bunk beds and a window"></div>
    <div class="events">
      <h2 class="events__title">EVENTS:</h2>
      <ul class="events__list">
        <li>Horseback Riding</li>
        <li>Low Ropes Course</li>
        <li>Hatchet Throwing</li>
        <li>Archery Tag</li>
        <li>Fishing</li>
        <li>Volleyball</li>
        <li>Softball</li>
        <li>Gaga Ball</li>
        <li>9 Square-in-the-Air</li>
        <li>Basketball</li>
        <li>Swimming (seasonal)</li>
        <li>Hiking</li>
        <li>Soccer</li>
      </ul>
    </div>
    <div class="ground" role="img" aria-label="Pine forest silhouette band"></div>
    <svg class="hex hex--cabins" width="170" height="160" viewBox="0 0 170 160">
      <defs>
        <linearGradient id="cabinsFill" x1="0" y1="0" x2="0" y2="1">
          <stop offset="0" stop-color="#7f9a6a"/><stop offset=".6" stop-color="#b4503a"/><stop offset="1" stop-color="#c9b9a4"/>
        </linearGradient>
      </defs>
      <polygon points="45,5 125,5 165,80 125,155 45,155 5,80" fill="url(#cabinsFill)" stroke="#1d3a24" stroke-width="6" role="img" aria-label="Photo of red cabins among trees"/>
    </svg>
  </section>

  <section class="panel panel--contact">
    <svg class="hex hex--pavilion" width="220" height="200" viewBox="0 0 220 200">
      <defs>
        <linearGradient id="pavilionFill" x1="0" y1="0" x2="0" y2="1">
          <stop offset="0" stop-color="#7fa86a"/><stop offset=".55" stop-color="#a98563"/><stop offset="1" stop-color="#c4c2bc"/>
        </linearGradient>
      </defs>
      <polygon points="55,6 165,6 214,100 165,194 55,194 6,100" fill="url(#pavilionFill)" stroke="#1d3a24" stroke-width="7" role="img" aria-label="Photo of an open-air pavilion under trees"/>
    </svg>
    <div class="book">
      <div class="book__title">BOOK</div>
      <div class="book__sub">YOUR RETREAT</div>
      <div class="book__call">CALL</div>
    </div>
    <div class="contact">
      <div class="contact__phone">501-555-0142</div>
      <div class="contact__or">OR</div>
      <div class="contact__label">EMAIL US AT</div>
      <div class="contact__email">jordan@campthornbury.org</div>
    </div>
    <div class="location">
      <div class="location__title">LOCATION</div>
      <div class="location__address">48 Millbrook Hollow Road Ridgeway, AR 72199</div>
      <div class="location__web">www.campthornbury.org</div>
    </div>
  </section>

  <section class="panel panel--cover">
    <div class="cover-photo" role="img" aria-label="Photo of a group of campers seen from behind on a rocky overlook at sunset above a forested valley"></div>
    <div class="brand">CAMP THORNBURY</div>
    <div class="social"><span></span><span></span></div>
  </section>

</main>
</body>
</html>
```